Criação de Logo + Papelaria + Manual Básico para Arquitetura
" Somos uma empresa pequena, eu e a minha sócia Clarice, atendemos o cliente, fazemos o levantamento de medidas e necessidades do cliente, desenvolvemos o projeto desde o início em 3D colorido, depois o projeto executivo e acompanhamento de obras. Estamos presentes no processo do início ao fim. Buscamos sempre atender o cliente da melhor maneira possível, sempre estando a par de todo o projeto. "

```html
<!DOCTYPE html>
<html lang="pt-BR">
<head>
<meta charset="utf-8">
<title>Lumen Estúdio — Cartão de visita</title>
<link rel="stylesheet" href="https://fonts.googleapis.com/css2?family=Josefin+Sans:wght@300;400&display=swap">
<style>
  :root {
    --backdrop: #e9e6e2;
    --card-grey: #7b7c7e;
    --card-white: #ffffff;
    --rose: #e2ab98;
    --ink-white: #ffffff;
    --tagline: #c9c9c9;
    --text-grey: #6f7072;
  }
  * { margin: 0; padding: 0; box-sizing: border-box; }
  html, body {
    width: 1200px;
    height: 1200px;
    overflow: hidden;
    background: var(--backdrop);
    font-family: "Josefin Sans", sans-serif;
  }
  .canvas {
    position: relative;
    width: 1200px;
    height: 1200px;
  }
  .card {
    position: absolute;
    width: 504px;
    height: 504px;
    box-shadow: 0 6px 18px rgba(0, 0, 0, 0.18);
  }
  .card-back {
    left: 509px;
    top: 504px;
    background: var(--card-white);
    z-index: 1;
  }
  .card-front {
    left: 192px;
    top: 192px;
    background: var(--card-grey);
    z-index: 2;
  }
  .front-lockup {
    position: absolute;
    left: 0;
    width: 100%;
    top: 118px;
    display: flex;
    flex-direction: column;
    align-items: center;
  }
  .brand {
    display: flex;
    align-items: center;
    gap: 14px;
    white-space: nowrap;
  }
  .brand-dot {
    width: 20px;
    height: 20px;
    border-radius: 50%;
    background: var(--rose);
  }
  .brand-name {
    color: var(--ink-white);
    font-weight: 300;
    font-size: 96px;
    letter-spacing: 4px;
    text-transform: uppercase;
    line-height: 1;
  }
  .brand-sub {
    margin-top: 30px;
    color: var(--ink-white);
    font-weight: 300;
    font-size: 44px;
    letter-spacing: 8px;
    text-transform: uppercase;
    line-height: 1;
    white-space: nowrap;
  }
  .tagline {
    margin-top: 14px;
    color: var(--tagline);
    font-weight: 300;
    font-size: 13px;
    letter-spacing: 3px;
    text-transform: uppercase;
    white-space: nowrap;
  }
  .back-brand {
    position: absolute;
    top: 382px;
    left: 0;
    width: 100%;
    text-align: center;
    color: var(--text-grey);
    font-weight: 300;
    font-size: 17px;
    letter-spacing: 3px;
    text-transform: uppercase;
  }
  .contact-line {
    position: absolute;
    left: 0;
    width: 100%;
    display: flex;
    align-items: center;
    justify-content: center;
    gap: 6px;
    color: var(--text-grey);
    font-weight: 400;
    font-size: 9.5px;
    white-space: nowrap;
  }
  .contact-line svg { width: 11px; height: 11px; fill: var(--text-grey); }
  .contact-address { top: 428px; }
  .contact-phone { top: 450px; }
</style>
</head>
<body>
<main class="canvas">
  <section class="card card-back">
    <p class="back-brand">Lumen</p>
    <p class="contact-line contact-address">
      <svg viewBox="0 0 24 24" aria-hidden="true"><path d="M12 2a7 7 0 0 0-7 7c0 5.2 7 13 7 13s7-7.8 7-13a7 7 0 0 0-7-7zm0 9.5A2.5 2.5 0 1 1 12 6.5a2.5 2.5 0 0 1 0 5z"/></svg>
      Rua das Acácias, 120 - Centro - Campo Verde - MS | Cep 79000-000
    </p>
    <p class="contact-line contact-phone">
      <svg viewBox="0 0 24 24" aria-hidden="true"><path d="M6.6 10.8a15.1 15.1 0 0 0 6.6 6.6l2.2-2.2a1 1 0 0 1 1-.25 11.4 11.4 0 0 0 3.6.57 1 1 0 0 1 1 1V20a1 1 0 0 1-1 1A17 17 0 0 1 3 4a1 1 0 0 1 1-1h3.5a1 1 0 0 1 1 1c0 1.25.2 2.45.57 3.57a1 1 0 0 1-.25 1z"/></svg>
      (67) 3000-0000
    </p>
  </section>

  <section class="card card-front">
    <div class="front-lockup">
      <div class="brand">
        <span class="brand-dot"></span>
        <span class="brand-name">Lumen</span>
      </div>
      <p class="brand-sub">Estúdio</p>
      <p class="tagline">Arquitetura e Interiores</p>
    </div>
  </section>
</main>
</body>
</html>
```